Frostwyn.co - Polar Expeditions Specialists

We need a modern, visually striking business card for Frostwyn.co, a company specialized in selling expedition cruises to the most remote regions on Earth, with a focus on the Arctic and Antarctica. The design should instantly communicate that the cardholder is an expert in polar travel. Use clean, premium aesthetics with cool tones like icy blue and white, possibly incorporating polar imagery (ice, glaciers, penguins, etc.)

Attached the logo

Contact Information for Business Card

Feels high-end and trustworthy.. Visually memorable — encourages people to keep it

Colors
0054AA
0677BA
7BADD7
CADEEF
E8F1F8

Requirements
Must have
• ice, glaciers, penguins, montains
Nice to have
• modern, transparente,

```html
<!DOCTYPE html>
<html lang="en">
<head>
<meta charset="UTF-8">
<title>Frostwyn.co Business Card</title>
<link href="https://fonts.googleapis.com/css2?family=Poppins:wght@400;600;700&display=swap" rel="stylesheet">
<style>
  :root {
    --page-bg: #e6e8eb;
    --card-white: #f7f7f6;
    --card-blue: #2b6fae;
    --ink: #15172a;
    --ink-soft: #4a4c5a;
    --white: #ffffff;
  }
  * { margin: 0; padding: 0; box-sizing: border-box; }
  html, body {
    width: 1200px; height: 800px; overflow: hidden;
    background: var(--page-bg);
    font-family: "Poppins", sans-serif;
  }
  .stage {
    width: 1200px; height: 800px;
    display: flex; flex-direction: column; align-items: center; justify-content: center;
    gap: 28px;
  }
  .card {
    width: 420px; height: 272px;
    position: relative;
    box-shadow: 0 6px 18px rgba(0,0,0,0.12);
  }
  .card-front { background: var(--card-white); color: var(--ink); }
  .card-back { background: var(--card-blue); color: var(--white); display: flex; align-items: center; justify-content: center; }

  .holder { position: absolute; left: 34px; top: 83px; }
  .holder-name { font-size: 16px; font-weight: 600; letter-spacing: 0.5px; line-height: 1.1; }
  .holder-role { font-size: 11px; color: var(--ink-soft); margin-top: 4px; }
  .contact-list { list-style: none; margin-top: 20px; }
  .contact-item { display: flex; align-items: center; gap: 9px; font-size: 11px; color: var(--ink-soft); height: 18px; }
  .contact-icon { width: 9px; height: 9px; flex: none; }

  .divider { position: absolute; left: 213px; top: 73px; width: 2px; height: 127px; background: var(--ink); }

  .brand { display: flex; flex-direction: column; align-items: center; }
  .card-front .brand { position: absolute; left: 228px; width: 180px; top: 80px; }
  .brand-dot { border-radius: 50%; background: currentColor; }
  .card-front .brand-dot { width: 40px; height: 40px; }
  .card-back .brand-dot { width: 48px; height: 48px; }
  .brand-name { font-weight: 700; line-height: 1; }
  .card-front .brand-name { font-size: 24px; margin-top: 11px; }
  .card-back .brand-name { font-size: 33px; margin-top: 13px; }
  .brand-tagline { font-weight: 600; }
  .card-front .brand-tagline { font-size: 8px; margin-top: 5px; }
  .card-back .brand-tagline { font-size: 10px; margin-top: 6px; }
</style>
</head>
<body>
<main class="stage">
  <section class="card card-front">
    <div class="holder">
      <h1 class="holder-name">MARTIN ILVES</h1>
      <p class="holder-role">Owner</p>
      <ul class="contact-list">
        <li class="contact-item">
          <svg class="contact-icon" viewBox="0 0 10 10"><rect x="2.5" y="0.5" width="5" height="9" rx="1" fill="none" stroke="#15172a" stroke-width="1.2"/></svg>
          155 480 902
        </li>
        <li class="contact-item">
          <svg class="contact-icon" viewBox="0 0 10 10"><rect x="0.5" y="2" width="9" height="6.5" fill="#15172a"/><path d="M0.5 2 L5 5.5 L9.5 2" fill="none" stroke="#f7f7f6" stroke-width="0.9"/></svg>
          info@frostwyn.co
        </li>
        <li class="contact-item">
          <svg class="contact-icon" viewBox="0 0 10 10"><circle cx="5" cy="5" r="4.3" fill="none" stroke="#15172a" stroke-width="1.2"/><circle cx="5" cy="5" r="1.6" fill="#15172a"/></svg>
          www.frostwyn.co
        </li>
      </ul>
    </div>
    <div class="divider"></div>
    <div class="brand">
      <span class="brand-dot"></span>
      <span class="brand-name">Frostwyn.co</span>
      <span class="brand-tagline">Polar Expeditions Specialists</span>
    </div>
  </section>

  <section class="card card-back">
    <div class="brand">
      <span class="brand-dot"></span>
      <span class="brand-name">Frostwyn.co</span>
      <span class="brand-tagline">Polar Expeditions Specialists</span>
    </div>
  </section>
</main>
</body>
</html>
```